Brisk Foundry PowerPoint Template

Project Title: Professional & Functional PowerPoint Template (.potx) – Brisk Foundry Rebrand

Project Overview:
Brisk Foundry has recently undergone a complete rebranding, including a new logo, website, and visual identity. We need a professional, high-end PowerPoint Template (.potx) that reflects our new look while being highly functional for everyday use.

We previously had a design created, but it was built incorrectly (static images, oversized file, no Master Slides). The goal of this project is to take our new aesthetic and build a "workable" template where layouts are controlled by Master Slides and text is easily editable.

Style & Brand Direction:
The template must be an extension of our new website: https://www.brisk-foundry.net/

Aesthetic: Modern, clean, high-tech, and "Industrial Tech."

Color Palette: Please pull the primary blues, greys, and accent colors directly from the website.

Imagery/Graphics: Use clean lines and subtle tech-inspired gradients. Avoid "clutter."

Tone: Innovative, precise, and professional.

Technical Requirements (Crucial)
Format: Must be delivered as a PowerPoint Template file (** .potx **).

Functionality: All layouts must be built using Slide Masters. Users should be able to click "New Slide" and choose from specific layouts.

Native Elements: Do NOT use full-page background images for text areas. Bullet points must use native PowerPoint list functionality (not individual text boxes).

File Size: The template must be optimized and lightweight.

Fonts: Use standard professional fonts or provide the specific web-safe equivalent used on our site (e.g., Montserrat, Open Sans, etc.).

Required Slide Layouts
Please include a minimum of 10–12 Master layouts, including:
*Title Slide (2-3 variations: Dark and Light)
*Agenda/Table of Contents
*Section Header/Divider Slides
*Standard Text/Bullet Slide
*Two-Column Text Slide
*Image + Text Layouts (Left/Right variations)
*Data/Chart Slide (Styled bar/pie charts that match the brand)
*Process/Timeline Slide (Infographic style)
*Section slide

Attachments Provided
Brand Assets (.zip): Contains our new logo in various formats.

Inspiration/Existing PPT: We have attached the previous design created by our web agency. Note: Use this for visual inspiration ONLY. Do not copy the file structure, as it is technically flawed.

Deliverables
Final .potx file.

All used icons or custom graphics in vector format (if applicable).

Instruction note on any specific fonts used.

Target Market(s)

Internal communication and external (investors, customers)

Industry/Entity Type

Semiconductor, Automotive

Requirements
Must have
• A potx file

```html
<!DOCTYPE html>
<html lang="en">
<head>
<meta charset="utf-8">
<title>Brisk Foundry – Presentation Template Overview</title>
<link href="https://fonts.googleapis.com/css2?family=Poppins:ital,wght@0,400;0,500;0,600;0,700;0,800;1,400;1,600&display=swap" rel="stylesheet">
<style>
:root{
  --blue:#1f3ff2;
  --ink:#151515;
  --panel:#1c1c1d;
  --grey:#8c8c8c;
  --light:#d8d8d8;
  --paper:#ffffff;
  --stage:#e3e4e6;
}
*{margin:0;padding:0;box-sizing:border-box}
html,body{width:1035px;height:1200px;overflow:hidden;background:var(--stage);font-family:'Poppins',sans-serif;color:var(--ink)}
.board{position:relative;width:1035px;height:1200px}
.slide{position:absolute;width:307px;height:172px;background:var(--paper);overflow:hidden;box-shadow:0 2px 5px rgba(0,0,0,.28)}
.slide.dark{background:var(--panel);color:#fff}
.c1{left:40px}.c2{left:364px}.c3{left:688px}
.r1{top:39px}.r2{top:229px}.r3{top:423px}.r4{top:613px}.r5{top:800px}.r6{top:991px}
.abs{position:absolute}
.h{position:absolute;left:13px;top:10px;font-size:10px;font-weight:400;white-space:nowrap}
.h b{font-weight:700}
.rule{position:absolute;left:13px;top:25px;width:24px;height:2.5px;border-radius:2px;background:var(--blue)}
.foot{position:absolute;left:10px;right:10px;top:155px;display:flex;align-items:flex-end;gap:3px}
.foot .sq{width:7px;height:7px;background:var(--blue)}
.foot .nm{font-size:5px;font-weight:700;line-height:1}
.foot .ln{flex:1;height:.5px;background:currentColor}
.foot .pg{font-size:3.5px;line-height:1;margin-bottom:-3px}
.tiny{font-size:3.3px;line-height:1.4;color:var(--grey)}
.dark .tiny{color:#b9b9b9}
.blue{color:var(--blue)}
.ph{position:absolute}
.ital{font-style:italic}
.member-name{font-size:5px;font-weight:700;margin-top:4px;white-space:nowrap}
</style>
</head>
<body>
<main class="board">

<!-- Title, dark -->
<section class="slide dark c1 r1">
  <div class="abs" style="left:16px;top:24px;display:flex;align-items:center;gap:4px">
    <span style="width:13px;height:13px;background:var(--blue)"></span>
    <span style="font-size:11px;font-weight:700;letter-spacing:.3px">BRISK FOUNDRY</span>
  </div>
  <div class="abs" style="left:16px;top:60px;line-height:1.1">
    <div class="blue" style="font-size:14px;font-weight:800">PRESENTATION</div>
    <div style="font-size:13px;font-weight:700">TITLE</div>
    <div style="font-size:13px">Goes Here</div>
    <div class="blue" style="font-size:7.5px;font-weight:700;margin-top:5px">Presentation Template</div>
    <div style="font-size:4.3px;line-height:1.3;margin-top:1px">Lorem ipsum is simply dummy<br>text of the printing<br>and typesetting industry.</div>
  </div>
  <div class="abs" style="left:16px;top:155px;font-size:4px;letter-spacing:.4px">Friday, July 18, 2025</div>
  <div class="abs" style="left:148px;top:15px;width:159px;height:142px;background:var(--blue)"></div>
  <div class="ph" role="img" aria-label="Black and white photo of a microscope over a silicon wafer" style="left:161px;top:28px;width:125px;height:115px;background:radial-gradient(circle at 50% 50%,#9a9a9a,#2a2a2a 70%,#111)"></div>
  <div class="abs" style="left:189px;top:26px;width:68px;height:2px;background:#fff"></div>
  <div class="abs" style="left:189px;top:142px;width:68px;height:2px;background:#fff"></div>
</section>

<!-- Title, light -->
<section class="slide c2 r1">
  <div class="abs" style="left:6px;top:6px;width:6px;height:6px;background:var(--blue)"></div>
  <div class="abs" style="left:19px;top:31px;display:flex;align-items:center;gap:4px">
    <span style="width:12px;height:12px;background:var(--blue)"></span>
    <span style="font-size:10px;font-weight:700">BRISK FOUNDRY</span>
  </div>
  <div class="abs" style="left:19px;top:66px;line-height:1">
    <div class="blue" style="font-size:15px;font-weight:800">Business</div>
    <div style="font-size:16px;font-weight:800">Marketing</div>
    <div class="blue ital" style="font-size:8px;font-weight:600;margin-top:3px">Presentation</div>
    <div class="tiny ital" style="margin-top:2px;font-size:3.8px">Lorem ipsum dolor sit amet, consectetuer<br>adipiscing elit, sed diam nonum</div>
  </div>
  <div class="abs" style="left:19px;top:155px;display:flex;gap:2px">
    <i style="width:3px;height:3px;border-radius:50%;background:var(--ink)"></i>
    <i style="width:3px;height:3px;border-radius:50%;background:var(--blue)"></i>
    <i style="width:3px;height:3px;border-radius:50%;background:var(--ink)"></i>
  </div>
  <div class="ph" role="img" aria-label="Photo of a robotic probe scanning a glowing blue wafer" style="left:129px;top:0;width:178px;height:140px;background:linear-gradient(160deg,#d6dce6,#7f9ab8 40%,#2f5d9c 75%,#12305e)"></div>
  <div class="abs" style="left:129px;top:140px;width:178px;height:32px;background:var(--ink);color:#fff;font-size:6px;letter-spacing:2px;text-align:center;line-height:32px">www.website.com</div>
</section>

<!-- Contents -->
<section class="slide c3 r1">
  <div class="h" style="top:11px">Table of <b>Contents</b></div>
  <div class="rule" style="top:27px"></div>
  <svg class="abs" style="left:25px;top:50px" width="260" height="90" viewBox="0 0 260 90">
    <g font-family="Poppins,sans-serif" font-size="4.5" font-weight="600" fill="#151515">
      <text x="3" y="5">Simple Text One</text>
      <text x="3" y="23">Simple Text Two</text>
      <text x="3" y="41">Simple Text Three</text>
      <text x="3" y="59">Simple Text Four</text>
      <text x="3" y="77">Simple Text Five</text>
      <g transform="translate(133 0)">
        <text x="3" y="5">Simple Text One</text>
        <text x="3" y="23">Simple Text Two</text>
        <text x="3" y="41">Simple Text Three</text>
        <text x="3" y="59">Simple Text Four</text>
        <text x="3" y="77">Simple Text Five</text>
      </g>
    </g>
    <g fill="#1f3ff2"><circle cx="0.5" cy="3.5" r="1"/><circle cx="0.5" cy="21.5" r="1"/><circle cx="0.5" cy="39.5" r="1"/><circle cx="0.5" cy="57.5" r="1"/><circle cx="0.5" cy="75.5" r="1"/>
      <circle cx="133.5" cy="3.5" r="1"/><circle cx="133.5" cy="21.5" r="1"/><circle cx="133.5" cy="39.5" r="1"/><circle cx="133.5" cy="57.5" r="1"/><circle cx="133.5" cy="75.5" r="1"/></g>
    <g stroke="#bbb" stroke-width=".4" stroke-dasharray="1 .8">
      <line x1="3" y1="7" x2="108" y2="7"/><line x1="3" y1="25" x2="108" y2="25"/><line x1="3" y1="43" x2="108" y2="43"/><line x1="3" y1="61" x2="108" y2="61"/><line x1="3" y1="79" x2="108" y2="79"/>
      <line x1="136" y1="7" x2="240" y2="7"/><line x1="136" y1="25" x2="240" y2="25"/><line x1="136" y1="43" x2="240" y2="43"/><line x1="136" y1="61" x2="240" y2="61"/><line x1="136" y1="79" x2="240" y2="79"/>
    </g>
    <g fill="#1f3ff2"><circle cx="112" cy="8" r="4"/><circle cx="112" cy="26" r="4"/><circle cx="112" cy="44" r="4"/><circle cx="112" cy="62" r="4"/><circle cx="112" cy="80" r="4"/>
      <circle cx="244" cy="8" r="4"/><circle cx="244" cy="26" r="4"/><circle cx="244" cy="44" r="4"/><circle cx="244" cy="62" r="4"/><circle cx="244" cy="80" r="4"/></g>
    <g font-family="Poppins,sans-serif" font-size="3.3" font-weight="700" fill="#fff" text-anchor="middle">
      <text x="112" y="9.2">02</text><text x="112" y="27.2">04</text><text x="112" y="45.2">06</text><text x="112" y="63.2">08</text><text x="112" y="81.2">10</text>
      <text x="244" y="9.2">02</text><text x="244" y="27.2">04</text><text x="244" y="45.2">06</text><text x="244" y="63.2">08</text><text x="244" y="81.2">10</text>
    </g>
  </svg>
  <div class="foot"><span class="sq"></span><span class="nm">BRISK FOUNDRY</span><span class="ln"></span><span class="pg">2</span></div>
</section>

<!-- Mission / Vision -->
<section class="slide c1 r2">
  <div class="h"><b>Heading</b> Goes Here</div><div class="rule"></div>
  <div class="abs ital" style="left:22px;top:39px;width:125px;font-size:4.6px;line-height:1.35;color:#444">Lorem ipsum dolor sit amet, cons ectetuer adipiscing elit, sed diam nonummy nibh euis-mod tincidunt.Lorem ipsum dolor sit amet.</div>
  <div class="ph" role="img" aria-label="Photo of a hand holding a glowing vision icon" style="left:22px;top:67px;width:126px;height:73px;border-radius:6px;background:radial-gradient(circle at 55% 45%,#6f8fe8,#1b3aa8 50%,#0b1a55)"></div>
  <div class="abs" style="left:163px;top:55px;width:26px;height:26px;border-radius:3px;background:var(--blue)"></div>
  <div class="abs" style="left:196px;top:55px;width:100px">
    <div style="font-size:6.5px;font-weight:600">Our Mission</div>
    <div class="tiny ital" style="font-size:3.8px">Lorem ipsum dolor sit amet, cons ectetuer adipiscing elit, sed diam nonummy nibh euismod tincidunt.</div>
  </div>
  <div class="abs" style="left:163px;top:104px;width:26px;height:26px;border-radius:3px;background:var(--blue)"></div>
  <div class="abs" style="left:196px;top:104px;width:100px">
    <div style="font-size:6.5px;font-weight:600">Our Vision</div>
    <div class="tiny ital" style="font-size:3.8px">Lorem ipsum dolor sit amet, cons ectetuer adipiscing elit, sed diam nonummy nibh euismod tincidunt.</div>
  </div>
  <svg class="abs" style="left:168px;top:60px" width="16" height="16" viewBox="0 0 16 16" fill="none" stroke="#fff" stroke-width="1.3"><path d="M3 10 L10 4 L12 6 L6 13 Z M3 10 L1 12 M11 2 L14 5"/></svg>
  <svg class="abs" style="left:168px;top:109px" width="16" height="16" viewBox="0 0 16 16" fill="none" stroke="#fff" stroke-width="1.3"><path d="M2 14 L14 2 M2 2 L14 14 M4 4 L6 2 M12 14 L14 12"/></svg>
  <div class="foot"><span class="sq"></span><span class="nm">BRISK FOUNDRY</span><span class="ln"></span><span class="pg">3</span></div>
</section>

<!-- Idea / Promotion / Growth -->
<section class="slide c2 r2">
  <div class="h"><b>Heading</b> Goes Here</div><div class="rule"></div>
  <div class="abs" style="left:0;top:31px;width:307px;height:120px;background:var(--panel)"></div>
  <svg class="abs" style="left:60px;top:44px" width="190" height="72" viewBox="0 0 190 72" fill="none" stroke="#1f3ff2" stroke-width="1.4">
    <rect x="6" y="3" width="46" height="66" rx="4"/>
    <rect x="70" y="3" width="46" height="66" rx="4"/>
    <rect x="133" y="3" width="46" height="66" rx="4"/>
    <path d="M52 18 L58 18 L58 10"/><circle cx="58" cy="9" r="2" fill="#1f3ff2"/>
    <path d="M52 55 L58 55 L70 30"/>
    <path d="M116 18 L124 18 L124 10"/><circle cx="124" cy="9" r="2" fill="#1f3ff2"/>
    <path d="M116 55 L133 30"/><circle cx="70" cy="55" r="2" fill="#1f3ff2"/><circle cx="133" cy="55" r="2" fill="#1f3ff2"/>
    <g font-family="Poppins,sans-serif" font-size="4.5" font-weight="700" fill="#fff" stroke="none" text-anchor="middle">
      <text x="29" y="28">IDEA</text><text x="93" y="28">PROMOTION</text><text x="156" y="28">GROWTH</text>
    </g>
  </svg>
  <div class="abs tiny" style="left:70px;top:76px;width:38px;font-size:2.6px;text-align:center">Lorem ipsum dolor sit amet, consectetuer adipiscing elit, sed diam nonummy nibh euismod tincidunt ut laoreet dolore magna aliquam erat volutpat.</div>
  <div class="abs tiny" style="left:134px;top:76px;width:38px;font-size:2.6px;text-align:center">Lorem ipsum dolor sit amet, consectetuer adipiscing elit, sed diam nonummy nibh euismod tincidunt ut laoreet dolore magna aliquam erat volutpat.</div>
  <div class="abs tiny" style="left:197px;top:76px;width:38px;font-size:2.6px;text-align:center">Lorem ipsum dolor sit amet, consectetuer adipiscing elit, sed diam nonummy nibh euismod tincidunt ut laoreet dolore magna aliquam erat volutpat.</div>
  <div class="abs" style="left:45px;top:124px;width:218px;font-size:3.3px;line-height:1.4;color:#fff;text-align:center">Lorem ipsum dolor sit amet, consectetuer adipiscing elit, sed diam nonummy nibh euismod tincidunt ut laoreet dolore magna aliquam erat volutpat. Ut wisi enim ad minim veniam, quis nostrud exerci tation ullamcorper suscipit lobortis nisl ut aliquip ex ea commodo consequat.</div>
  <div class="foot"><span class="sq"></span><span class="nm">BRISK FOUNDRY</span><span class="ln"></span><span class="pg">4</span></div>
</section>

<!-- Numbered list + dark card -->
<section class="slide c3 r2">
  <div class="h"><b>Heading</b> Goes Here</div><div class="rule"></div>
  <div class="abs" style="left:37px;top:37px;width:110px;font-size:4.6px;line-height:1.2">
    <div><b class="blue">01.</b> <b>Aliquam Erat Volutpat</b><div class="tiny">Lorem ipsum dolor sit amet, consectetuer adipiscing elit, sed diam nonummy nibh euismod</div></div>
    <div style="margin-top:11px"><b class="blue">02.</b> <b>Consectetuer Adipiscing Elit</b><div class="tiny">Lorem ipsum dolor sit amet, consectetuer adipiscing elit, sed diam nonummy nibh euismod tincidunt ut laoreet</div></div>
    <div style="margin-top:9px"><b class="blue">03.</b> <b>Duis Autem Vel Eum</b><div class="tiny">Lorem ipsum dolor sit amet, consectetuer adipiscing elit, sed diam nonummy nibh euismod tincidunt.</div></div>
    <div style="margin-top:11px"><b class="blue">04.</b> <b>Aliquam Erat Volutpat</b><div class="tiny">Lorem ipsum dolor sit amet, consectetuer adipiscing elit, sed diam nonummy nibh euismod tincidunt ut laoreet.</div></div>
  </div>
  <div class="abs" style="left:170px;top:34px;width:106px;height:107px;border-radius:7px;background:var(--panel)"></div>
  <div class="abs" style="left:159px;top:46px;display:flex;flex-direction:column;gap:13px">
    <span style="width:20px;height:20px;border-radius:50%;background:var(--blue);border:2px solid #fff"></span>
    <span style="width:20px;height:20px;border-radius:50%;background:var(--blue);border:2px solid #fff"></span>
    <span style="width:20px;height:20px;border-radius:50%;background:var(--blue);border:2px solid #fff"></span>
  </div>
  <div class="abs" style="left:189px;top:44px;width:85px;color:#fff">
    <div class="blue" style="font-size:6px;font-weight:500">LOREM IPSUM</div><div style="font-size:3.2px;line-height:1.3">ipsum dolor sit amet, cons ectetuer adipiscing elit, sed diam nonummy nibh euismod tincidunt ut laoreet</div>
    <div class="blue" style="font-size:6px;font-weight:500;margin-top:6px">LOREM IPSUM</div><div style="font-size:3.2px;line-height:1.3">ipsum dolor sit amet, cons ectetuer adipiscing elit, sed diam nonummy nibh euismod tincidunt ut laoreet dolore magna aliquam erat volutpat.</div>
    <div class="blue" style="font-size:6px;font-weight:500;margin-top:5px">LOREM IPSUM</div><div style="font-size:3.2px;line-height:1.3">ipsum dolor sit amet, cons ectetuer adipiscing elit, sed diam nonummy nibh euismod tincidunt</div>
  </div>
  <div class="foot"><span class="sq"></span><span class="nm">BRISK FOUNDRY</span><span class="ln"></span><span class="pg">5</span></div>
</section>

<!-- Problem / Solution grid -->
<section class="slide c1 r3">
  <div class="h"><b>Heading</b> Goes Here</div><div class="rule"></div>
  <div class="abs" style="left:22px;top:55px;width:150px;display:grid;grid-template-columns:1fr 1fr;column-gap:10px;row-gap:14px;font-size:5.5px">
    <div><b class="blue">01.</b> <b>Project Problem</b><div class="tiny" style="color:#bbb">Lorem ipsum dolor sit amet, cons ectetuer adipiscing elit, sed diam nonummy nibh euismod tincidunt.Lorem ipsum dolor sit amet.</div></div>
    <div><b class="blue">02.</b> <b>Project Solution</b><div class="tiny" style="color:#bbb">Lorem ipsum dolor sit amet, cons ectetuer adipiscing elit, sed diam nonummy nibh euismod tincidunt.Lorem ipsum dolor sit amet.</div></div>
    <div><b class="blue">03.</b> <b>Project Problem</b><div class="tiny" style="color:#bbb">Lorem ipsum dolor sit amet, cons ectetuer adipiscing elit, sed diam nonummy nibh euismod tincidunt.Lorem ipsum dolor sit amet.</div></div>
    <div><b class="blue">04.</b> <b>Project Solution</b><div class="tiny" style="color:#bbb">Lorem ipsum dolor sit amet, cons ectetuer adipiscing elit, sed diam nonummy nibh euismod tincidunt.Lorem ipsum dolor sit amet.</div></div>
  </div>
  <div class="abs" style="left:184px;top:39px;width:102px;height:98px;display:grid;grid-template-columns:1fr 1fr;gap:3px;color:#fff">
    <div style="background:var(--blue);border-radius:3px 0 0 0;padding:22px 6px 0"><div style="font-size:4.8px;font-weight:700">PROBLEM</div><div style="font-size:2.6px;line-height:1.4">Lorem ipsum dolor sit amet, cons ectetuer adipiscing elit, sed diam nonummy.</div></div>
    <div style="background:var(--ink);border-radius:0 3px 0 0;padding:22px 6px 0"><div style="font-size:4.8px;font-weight:700">SOLUTION</div><div style="font-size:2.6px;line-height:1.4">Lorem ipsum dolor sit amet, cons ectetuer adipiscing elit, sed diam nonummy.</div></div>
    <div style="background:var(--ink);border-radius:0 0 0 3px;padding:20px 6px 0"><div style="font-size:4.8px;font-weight:700">MARKET</div><div style="font-size:2.6px;line-height:1.4">Lorem ipsum dolor sit amet, cons ectetuer adipiscing elit, sed diam nonummy.</div></div>
    <div style="background:var(--blue);border-radius:0 0 3px 0;padding:20px 6px 0"><div style="font-size:4.8px;font-weight:700">MISSION</div><div style="font-size:2.6px;line-height:1.4">Lorem ipsum dolor sit amet, cons ectetuer adipiscing elit, sed diam nonummy.</div></div>
  </div>
  <div class="foot"><span class="sq"></span><span class="nm">BRISK FOUNDRY</span><span class="ln"></span><span class="pg">6</span></div>
</section>

<!-- Section divider -->
<section class="slide dark c2 r3" style="background:radial-gradient(ellipse at 70% 30%,#3a3a3c,#161617 70%)">
  <div class="abs" style="left:32px;top:42px;width:91px;height:90px;background:var(--blue)"></div>
  <div class="abs blue" style="left:137px;top:66px;font-size:38px;font-weight:800;line-height:1">01</div>
  <div class="abs" style="left:185px;top:67px;width:100px">
    <div class="blue" style="font-size:12px;font-weight:700;line-height:1">Part One.</div>
    <div style="font-size:4.8px;line-height:1.3;margin-top:2px">Lorem ipsumectetuer adipiscing elit sed diam nonummy nibh euismod tincidunt</div>
  </div>
</section>

<!-- Image + text -->
<section class="slide c3 r3">
  <div class="h"><b>Heading</b> Goes Here</div><div class="rule"></div>
  <div class="ph" role="img" aria-label="Photo of an engineer with a laptop in a server room" style="left:31px;top:37px;width:101px;height:107px;border-radius:6px;background:linear-gradient(90deg,#0d2446,#2a5d96 50%,#0d2446)"></div>
  <div class="abs" style="left:145px;top:39px;width:131px">
    <div style="font-size:7px;font-weight:500"><b class="blue">01.</b> Text Added Here</div>
    <div class="tiny" style="text-align:justify">Lorem ipsum dolor sit amet, cons ectetuer adipiscing elit, sed diam nonummy nibh euismod tincidunt ut laoreet dolore magna aliquam erat volutpat. Ut wisi enim ad minim veniam, quis nostrud exerci tation ullamcorper suscipit lobortis nisl ut aliquip ex ea commodo consequat.</div>
    <div style="font-size:7px;font-weight:500;margin-top:4px"><b class="blue">02.</b> Text Added Here</div>
    <div class="tiny" style="text-align:justify">Lorem ipsum dolor sit amet, cons ectetuer adipiscing elit, sed diam nonummy nibh euismod tincidunt ut laoreet dolore magna aliquam erat volutpat. Ut wisi enim ad minim veniam, quis nostrud exerci tation ullamcorper suscipit lobortis nisl ut aliquip ex ea commodo consequat.</div>
    <div style="font-size:7px;font-weight:500;margin-top:7px"><b class="blue">03.</b> Text Added Here</div>
    <div class="tiny" style="text-align:justify">Lorem ipsum dolor sit amet, cons ectetuer adipiscing elit, sed diam nonummy nibh euismod tincidunt ut laoreet dolore magna aliquam erat volutpat. Ut wisi enim ad minim veniam, quis nostrud exerci tation ullamcorper suscipit lobortis nisl ut aliquip ex ea commodo consequat.</div>
  </div>
  <div class="foot"><span class="sq"></span><span class="nm">BRISK FOUNDRY</span><span class="ln"></span><span class="pg">8</span></div>
</section>

<!-- Chart -->
<section class="slide dark c1 r4">
  <div class="h"><b>Heading</b> Goes Here</div><div class="rule"></div>
  <svg class="abs" style="left:20px;top:38px" width="135" height="100" viewBox="0 0 135 100">
    <g stroke="#333" stroke-width=".3"><line x1="8" y1="9" x2="130" y2="9"/><line x1="8" y1="23" x2="130" y2="23"/><line x1="8" y1="36" x2="130" y2="36"/><line x1="8" y1="49" x2="130" y2="49"/><line x1="8" y1="63" x2="130" y2="63"/><line x1="8" y1="76" x2="130" y2="76"/><line x1="8" y1="89" x2="130" y2="89" stroke="#666"/></g>
    <g font-family="Poppins,sans-serif" font-size="2.5" fill="#999" text-anchor="end"><text x="5" y="10">6</text><text x="5" y="24">5</text><text x="5" y="37">4</text><text x="5" y="50">3</text><text x="5" y="64">2</text><text x="5" y="77">1</text><text x="5" y="90">0</text></g>
    <rect x="16" y="27" width="6" height="62" fill="#1f3ff2"/><rect x="23" y="39" width="6" height="50" fill="#7a7a7a"/><rect x="30" y="56" width="6" height="33" fill="#d0d0d0"/>
    <rect x="54" y="27" width="6" height="62" fill="#1f3ff2"/><rect x="61" y="8" width="6" height="81" fill="#7a7a7a"/><rect x="68" y="42" width="6" height="47" fill="#d0d0d0"/>
    <rect x="92" y="23" width="6" height="66" fill="#1f3ff2"/><rect x="99" y="56" width="6" height="33" fill="#7a7a7a"/><rect x="106" y="42" width="6" height="47" fill="#d0d0d0"/>
    <g font-family="Poppins,sans-serif" font-size="3" fill="#bbb" text-anchor="middle"><text x="26" y="95">Category 1</text><text x="64" y="95">Category 1</text><text x="102" y="95">Category 1</text></g>
    <g font-family="Poppins,sans-serif" font-size="1.9" fill="#999"><rect x="43" y="97.5" width="1.5" height="1.5" fill="#1f3ff2"/><text x="45.5" y="99">Series 1</text><rect x="55" y="97.5" width="1.5" height="1.5" fill="#7a7a7a"/><text x="57.5" y="99">Series 2</text><rect x="67" y="97.5" width="1.5" height="1.5" fill="#d0d0d0"/><text x="69.5" y="99">Series 3</text></g>
  </svg>
  <div class="abs" style="left:160px;top:39px;width:135px">
    <div style="display:flex;gap:7px;align-items:flex-start"><span style="flex:none;width:15px;height:15px;border-radius:50%;background:var(--blue);font-size:7px;font-weight:700;text-align:center;line-height:15px;margin-top:2px">1</span><div><div class="blue" style="font-size:6px;font-weight:600">Lorem ipsum dolor.</div><div class="ital" style="font-size:3.9px;line-height:1.35">Lorem ipsumectetuer adipiscing elit, sed diam nonummy nibh euismod tincidunt sed diam nonummy nibhunt</div></div></div>
    <div style="display:flex;gap:7px;align-items:flex-start;margin-top:8px"><span style="flex:none;width:15px;height:15px;border-radius:50%;background:var(--blue);font-size:7px;font-weight:700;text-align:center;line-height:15px;margin-top:2px">2</span><div><div class="blue" style="font-size:6px;font-weight:600">Lorem ipsum dolor.</div><div class="ital" style="font-size:3.9px;line-height:1.35">Lorem ipsumectetuer adipiscing elit, sed diam nonummy nibh euismod tincidunt sed diam nonummy nibhunt</div></div></div>
    <div style="display:flex;gap:7px;align-items:flex-start;margin-top:8px"><span style="flex:none;width:15px;height:15px;border-radius:50%;background:var(--blue);font-size:7px;font-weight:700;text-align:center;line-height:15px;margin-top:2px">3</span><div><div class="blue" style="font-size:6px;font-weight:600">Lorem ipsum dolor.</div><div class="ital" style="font-size:3.9px;line-height:1.35">Lorem ipsumectetuer adipiscing elit, sed diam nonummy nibh euismod tincidunt sed diam nonummy nibhunt</div></div></div>
  </div>
  <div class="foot"><span class="sq"></span><span class="nm">BRISK FOUNDRY</span><span class="ln"></span><span class="pg">9</span></div>
</section>

<!-- Cycle -->
<section class="slide c2 r4">
  <div class="h"><b>Heading</b> Goes Here</div><div class="rule"></div>
  <svg class="abs" style="left:110px;top:46px" width="88" height="88" viewBox="0 0 100 100">
    <g stroke="#fff" stroke-width="2">
      <path d="M50 8 A42 42 0 0 0 8 50 L28 50 A22 22 0 0 1 50 28 Z" fill="#151515"/>
      <path d="M50 8 A42 42 0 0 1 92 50 L72 50 A22 22 0 0 0 50 28 Z" fill="#1f3ff2"/>
      <path d="M92 50 A42 42 0 0 1 50 92 L50 72 A22 22 0 0 0 72 50 Z" fill="#151515"/>
      <path d="M50 92 A42 42 0 0 1 8 50 L28 50 A22 22 0 0 0 50 72 Z" fill="#1f3ff2"/>
    </g>
    <g fill="none" stroke="#fff" stroke-width="1.3"><circle cx="33" cy="33" r="5"/><circle cx="67" cy="67" r="5"/><circle cx="33" cy="67" r="5"/><circle cx="67" cy="33" r="5"/></g>
    <g font-family="Poppins,sans-serif" font-size="8" font-weight="700" fill="#151515" text-anchor="middle"><text x="50" y="49">Text</text><text x="50" y="58">Added</text></g>
  </svg>
  <div class="abs" style="left:25px;top:50px;width:78px;text-align:right"><div class="blue" style="font-size:6.5px;font-weight:700">Text Here</div><div class="tiny">Lorem ipsum dolor sit amet, consectetuer adipiscing elit, sed diammy nibh euismod tincidunt ut laoreet dolore</div></div>
  <div class="abs" style="left:25px;top:111px;width:78px;text-align:right"><div style="font-size:6.5px;font-weight:700">Text Here</div><div class="tiny">Lorem ipsum dolor sit amet, consectetuer adipiscing elit, sed diammy nibh euismod tincidunt ut laoreet dolore</div></div>
  <div class="abs" style="left:205px;top:50px;width:80px"><div style="font-size:6.5px;font-weight:700">Text Here</div><div class="tiny">Lorem ipsum dolor sit amet, consectetuer adipiscing elit, sed diammy nibh euismod tincidunt ut laoreet dolore</div></div>
  <div class="abs" style="left:205px;top:111px;width:80px"><div class="blue" style="font-size:6.5px;font-weight:700">Text Here</div><div class="tiny">Lorem ipsum dolor sit amet, consectetuer adipiscing elit, sed diammy nibh euismod tincidunt ut laoreet dolore</div></div>
  <div class="foot"><span class="sq"></span><span class="nm">BRISK FOUNDRY</span><span class="ln"></span><span class="pg">10</span></div>
</section>

<!-- Text + bullets, dark -->
<section class="slide dark c3 r4">
  <div class="h"><b>Heading</b> Goes Here</div><div class="rule"></div>
  <div class="abs" style="left:28px;top:37px;width:125px">
    <div class="blue" style="font-size:7px;font-weight:500">01. Text Added Here</div>
    <div class="tiny" style="text-align:justify">Lorem ipsum dolor sit amet, cons ectetuer adipiscing elit, sed diam nonummy nibh euismod tincidunt ut laoreet dolore magna aliquam erat volutpat. Ut wisi enim ad minim veniam, quis nostrud exerci tation ullamcorper suscipit lobortis nisl ut aliquip ex ea commodo consequat.</div>
    <div class="tiny" style="text-align:justify;margin-top:3px">Lorem ipsum dolor sit amet, cons ectetuer adipiscing elit, sed diam tation ullamcorper suscipit lobortis nisl ut aliquip ex ea commodo consequat.</div>
    <div class="blue" style="font-size:7px;font-weight:500;margin-top:6px">02. Text Added Here</div>
    <div class="tiny" style="text-align:justify">Lorem ipsum dolor sit amet, cons ectetuer adipiscing elit, sed diam nonummy nibh euismod tincidunt ut laoreet dolore magna aliquam erat volutpat consequat.</div>
    <div class="tiny" style="text-align:justify;margin-top:3px">Lorem ipsum dolor sit amet, consectetuer adipiscing elit, sed diam nonummy nibh euismod tincidunt ut laoreet dolore magna aliquam erat volutpat. Ut wisi enim ad minim veniam, quis nostrud exerci tation</div>
  </div>
  <ul class="abs" style="left:167px;top:50px;list-style:none;font-size:6.3px;line-height:16.4px">
    <li><span class="blue">•</span> Fits Your Business Or Products</li>
    <li><span class="blue">•</span> Is Easy To Spell And Remember</li>
    <li><span class="blue">•</span> Fits Your Business Or Products</li>
    <li><span class="blue">•</span> Is Easy To Spell And Remember</li>
    <li><span class="blue">•</span> Fits Your Business Or Products</li>
    <li><span class="blue">•</span> Is Easy To Spell And Remember</li>
  </ul>
  <div class="foot"><span class="sq"></span><span class="nm">BRISK FOUNDRY</span><span class="ln"></span><span class="pg">11</span></div>
</section>

<!-- Timeline -->
<section class="slide c1 r5">
  <div class="h"><b>Heading</b> Goes Here</div><div class="rule"></div>
  <svg class="abs" style="left:0;top:40px" width="307" height="100" viewBox="0 0 307 100">
    <g font-family="Poppins,sans-serif" text-anchor="middle">
      <g font-size="4.6" font-weight="700" fill="#151515"><text x="55" y="6">YOUR TITLE</text><text x="154" y="6">YOUR TITLE</text><text x="254" y="6">YOUR TITLE</text></g>
      <g font-size="3.6" fill="#999"><text x="55" y="11">Refers to a good or</text><text x="55" y="15.5">service being offered</text><text x="154" y="11">Refers to a good or</text><text x="154" y="15.5">service being offered</text><text x="254" y="11">Refers to a good or</text><text x="254" y="15.5">service being offered</text></g>
    </g>
    <g stroke="#151515" stroke-width="1"><line x1="55" y1="23" x2="55" y2="33"/><line x1="154" y1="23" x2="154" y2="33"/><line x1="254" y1="23" x2="254" y2="33"/></g>
    <g fill="#151515"><circle cx="55" cy="23" r="2"/><circle cx="154" cy="23" r="2"/><circle cx="254" cy="23" r="2"/></g>
    <polygon points="36,36 76,36 81,45 28,45" fill="#1f3ff2"/>
    <polygon points="78,36 129,36 121,45 86,45" fill="#151515"/>
    <polygon points="135,36 175,36 180,45 127,45" fill="#1f3ff2"/>
    <polygon points="177,36 228,36 220,45 185,45" fill="#151515"/>
    <polygon points="234,36 274,36 279,45 226,45" fill="#1f3ff2"/>
    <g font-family="Poppins,sans-serif" font-size="4.6" font-weight="600" fill="#fff" text-anchor="middle"><text x="55" y="42.5">1990</text><text x="104" y="42.5">2001</text><text x="154" y="42.5">2007</text><text x="203" y="42.5">2012</text><text x="253" y="42.5">2020</text></g>
    <g stroke="#1f3ff2" stroke-width="1"><line x1="104" y1="50" x2="104" y2="60"/><line x1="203" y1="50" x2="203" y2="60"/></g>
    <g fill="#1f3ff2"><circle cx="104" cy="60" r="2"/><circle cx="203" cy="60" r="2"/></g>
    <g font-family="Poppins,sans-serif" text-anchor="middle">
      <g font-size="4.6" font-weight="700" fill="#1f3ff2"><text x="104" y="72">YOUR TITLE</text><text x="203" y="72">YOUR TITLE</text></g>
      <g font-size="3.6" fill="#999"><text x="104" y="77">Refers to a good or</text><text x="104" y="81.5">service being offered</text><text x="203" y="77">Refers to a good or</text><text x="203" y="81.5">service being offered</text></g>
    </g>
  </svg>
  <div class="foot"><span class="sq"></span><span class="nm">BRISK FOUNDRY</span><span class="ln"></span><span class="pg">12</span></div>
</section>

<!-- Two columns, dark -->
<section class="slide dark c2 r5">
  <div class="h"><b>Heading</b> Goes Here</div><div class="rule"></div>
  <div class="abs" style="left:28px;top:40px;width:251px;display:grid;grid-template-columns:1fr 1fr;column-gap:15px">
    <div>
      <div class="blue" style="font-size:7px;font-weight:500">01. Text Added Here</div>
      <div class="tiny" style="text-align:justify">Lorem ipsum dolor sit amet, cons ectetuer adipiscing elit, sed diam nonummy nibh euismod tincidunt ut laoreet dolore magna aliquam erat volutpat. Ut wisi enim ad minim veniam, quis nostrud exerci tation ullamcorper suscipit lobortis nisl ut aliquip ex ea commodo consequat. Lorem ipsum dolor sit amet, consectetuer adipiscing elit, sed diam nonummy nibh euismod tincidunt ut laoreet dolore magna aliquam erat volutpat.</div>
      <div class="tiny" style="text-align:justify;margin-top:5px">Lorem ipsum dolor sit amet, consectetuer adipiscing elit, sed diam nonummy nibh euismod tincidunt ut laoreet dolore magna aliquam erat volutpat. Ut wisi enim ad minim veniam, quis nostrud exerci tation ullamcorper suscipit lobortis nisl ut aliquip ex ea commodo consequat.</div>
      <div class="tiny" style="text-align:justify;margin-top:5px">Lorem ipsum dolor sit amet, consectetuer adipiscing elit, sed diam nonummy nibh euismod tincidunt ut laoreet dolore magna aliquam erat volutpat. Ut wisi enim ad minim veniam, quis nostrud exerci tation ullamcorper suscipit lobortis nisl ut aliquip.</div>
    </div>
    <div>
      <div class="blue" style="font-size:7px;font-weight:500">02. Text Added Here</div>
      <div class="tiny" style="text-align:justify">Lorem ipsum dolor sit amet, cons ectetuer adipiscing elit, sed diam nonummy nibh euismod tincidunt ut laoreet dolore magna aliquam erat volutpat. Ut wisi enim ad minim veniam, quis nostrud exerci tation ullamcorper suscipit lobortis nisl ut aliquip ex ea commodo consequat. Lorem ipsum dolor sit amet, consectetuer adipiscing elit, sed diam nonummy nibh euismod tincidunt ut laoreet dolore magna aliquam erat volutpat.</div>
      <div class="tiny" style="text-align:justify;margin-top:5px">Lorem ipsum dolor sit amet, consectetuer adipiscing elit, sed diam nonummy nibh euismod tincidunt ut laoreet dolore magna aliquam erat volutpat. Ut wisi enim ad minim veniam, quis nostrud exerci tation ullamcorper suscipit lobortis nisl ut aliquip ex ea commodo consequat.</div>
      <div class="tiny" style="text-align:justify;margin-top:5px">Lorem ipsum dolor sit amet, consectetuer adipiscing elit, sed diam nonummy nibh euismod tincidunt ut laoreet dolore magna aliquam erat volutpat. Ut wisi enim ad minim veniam, quis nostrud exerci tation ullamcorper suscipit lobortis nisl ut aliquip.</div>
    </div>
  </div>
  <div class="foot"><span class="sq"></span><span class="nm">BRISK FOUNDRY</span><span class="ln"></span><span class="pg">13</span></div>
</section>

<!-- Steps -->
<section class="slide c3 r5">
  <div class="h"><b>Heading</b> Goes Here</div><div class="rule"></div>
  <svg class="abs" style="left:0;top:40px" width="307" height="110" viewBox="0 0 307 110">
    <line x1="23" y1="41" x2="118" y2="41" stroke="#151515" stroke-width="3"/>
    <line x1="118" y1="41" x2="170" y2="41" stroke="#1f3ff2" stroke-width="3"/>
    <line x1="170" y1="41" x2="222" y2="41" stroke="#151515" stroke-width="3"/>
    <polygon points="222,39.5 280,39.5 280,37 286,41 280,45 280,42.5 222,42.5" fill="#1f3ff2"/>
    <g fill="none" stroke-width="4.5">
      <circle cx="74" cy="24" r="16" stroke="#151515"/>
      <circle cx="128" cy="24" r="16" stroke="#1f3ff2"/>
      <circle cx="182" cy="24" r="16" stroke="#151515"/>
      <circle cx="236" cy="24" r="16" stroke="#1f3ff2"/>
    </g>
    <g fill="#fff"><rect x="54" y="27" width="40" height="16"/><rect x="108" y="27" width="40" height="16"/><rect x="162" y="27" width="40" height="16"/><rect x="216" y="27" width="40" height="16"/></g>
    <rect x="50" y="39" width="47" height="5" fill="#151515"/><rect x="104" y="39" width="47" height="5" fill="#1f3ff2"/><rect x="158" y="39" width="47" height="5" fill="#151515"/><rect x="212" y="39" width="47" height="5" fill="#1f3ff2"/>
    <circle cx="74" cy="24" r="9" fill="#1f3ff2"/>
    <circle cx="128" cy="24" r="9" fill="#151515"/>
    <circle cx="182" cy="24" r="9" fill="#1f3ff2"/>
    <circle cx="236" cy="24" r="9" fill="#151515"/>
    <g fill="none" stroke="#fff" stroke-width="1"><circle cx="74" cy="24" r="5"/><path d="M74 21 V24 H76.5"/><circle cx="235" cy="23" r="3.5"/><path d="M237.5 25.5 L240 28"/><ellipse cx="182" cy="21" rx="4" ry="1.5"/><path d="M178 21 V27 M186 21 V27"/><ellipse cx="182" cy="27" rx="4" ry="1.5"/></g>
    <text x="128" y="26.5" font-family="Poppins,sans-serif" font-size="7" font-weight="700" fill="#fff" text-anchor="middle">$</text>
    <g font-family="Poppins,sans-serif" font-size="3.4" font-weight="700" fill="#fff" text-anchor="middle"><text x="74" y="42.6">Step 01</text><text x="128" y="42.6">Step 02</text><text x="182" y="42.6">Step 03</text><text x="236" y="42.6">Step 04</text></g>
    <g stroke="#151515" stroke-width=".8"><line x1="74" y1="46" x2="74" y2="54"/><line x1="128" y1="46" x2="128" y2="54"/><line x1="182" y1="46" x2="182" y2="54"/><line x1="236" y1="46" x2="236" y2="54"/></g>
    <g font-family="Poppins,sans-serif" text-anchor="middle">
      <g font-size="4.8" font-weight="700" fill="#151515"><text x="74" y="63">LOREM IPSUM</text><text x="128" y="63">LOREM IPSUM</text><text x="182" y="63">LOREM IPSUM</text><text x="236" y="63">LOREM IPSUM</text></g>
      <g font-size="2.6" fill="#999">
        <text x="74" y="68">Lorem ipsum dolor sit</text><text x="74" y="71.5">amet, consectetuer</text><text x="74" y="75">adipiscing elit, sed diam</text><text x="74" y="78.5">nonummy nibh euismod</text><text x="74" y="82">tincidunt ut laoreet</text>
        <text x="128" y="68">Lorem ipsum dolor sit</text><text x="128" y="71.5">amet, consectetuer</text><text x="128" y="75">adipiscing elit, sed diam</text><text x="128" y="78.5">nonummy nibh euismod</text><text x="128" y="82">tincidunt ut laoreet</text>
        <text x="182" y="68">Lorem ipsum dolor sit</text><text x="182" y="71.5">amet, consectetuer</text><text x="182" y="75">adipiscing elit, sed diam</text><text x="182" y="78.5">nonummy nibh euismod</text><text x="182" y="82">tincidunt ut laoreet</text>
        <text x="236" y="68">Lorem ipsum dolor sit</text><text x="236" y="71.5">amet, consectetuer</text><text x="236" y="75">adipiscing elit, sed diam</text><text x="236" y="78.5">nonummy nibh euismod</text><text x="236" y="82">tincidunt ut laoreet</text>
      </g>
    </g>
  </svg>
  <div class="foot"><span class="sq"></span><span class="nm">BRISK FOUNDRY</span><span class="ln"></span><span class="pg">14</span></div>
</section>

<!-- App screens -->
<section class="slide c1 r6">
  <div class="h"><b>Heading</b> Goes Here</div><div class="rule"></div>
  <div class="abs" style="left:13px;top:33px;width:118px">
    <div class="tiny" style="font-size:3.5px">Lorem ipsum dolor sit amet, consectetuer adipiscing elit, sed diam nonummy nibh euismod tincidunt ut laoreet dolore magna aliquam erat volutpat. Ut wisi enim ad minim veniam,</div>
    <div class="tiny" style="font-size:3.5px;margin-top:4px">quis nostrud exerci tation ullamcorper suscipit lobortis nisl ut aliquip ex ea commodo consequat. Duis autem vel eum iriure dolor in hendrerit in vulputate velit esse</div>
  </div>
  <div class="abs" style="left:23px;top:87px;display:flex;flex-direction:column;gap:11px">
    <div style="display:flex;gap:5px;align-items:flex-start"><span style="width:9px;height:9px;background:var(--ink);color:#fff;font-size:5px;font-weight:700;text-align:center;line-height:9px">1.</span><div><div class="blue" style="font-size:4.8px;font-weight:700">Lorem Ipsum</div><div class="tiny" style="font-size:2.6px">Lorem ipsum dolor sit amet, consectetuer adipiscing<br>elit, sed diam nonummy nibh euismod tincid</div></div></div>
    <div style="display:flex;gap:5px;align-items:flex-start"><span style="width:9px;height:9px;background:var(--ink);color:#fff;font-size:5px;font-weight:700;text-align:center;line-height:9px">2.</span><div><div class="blue" style="font-size:4.8px;font-weight:700">Lorem Ipsum</div><div class="tiny" style="font-size:2.6px">Lorem ipsum dolor sit amet, consectetuer adipiscing<br>elit, sed diam nonummy nibh euismod tincid</div></div></div>
    <div style="display:flex;gap:5px;align-items:flex-start"><span style="width:9px;height:9px;background:var(--ink);color:#fff;font-size:5px;font-weight:700;text-align:center;line-height:9px">3.</span><div><div class="blue" style="font-size:4.8px;font-weight:700">Lorem Ipsum</div><div class="tiny" style="font-size:2.6px">Lorem ipsum dolor sit amet, consectetuer adipiscing<br>elit, sed diam nonummy nibh euismod tincid</div></div></div>
  </div>
  <div class="ph" role="img" aria-label="Three smartphone screens showing app content over a faint radiating backdrop" style="left:170px;top:27px;width:130px;height:122px;background:radial-gradient(circle at 50% 55%,#f2f3f5,#ffffff 70%)"></div>
  <div class="abs" style="left:146px;top:28px;width:33px;height:68px;border:1.2px solid var(--ink);border-radius:4px;background:#fff;padding:8px 3px 0;font-size:4px;font-weight:500;line-height:1.15">Lorem ipsum dolor</div>
  <div class="abs" style="left:189px;top:50px;width:33px;height:68px;border:1.2px solid var(--ink);border-radius:4px;background:#fff;padding:8px 3px 0;font-size:4px;font-weight:500;line-height:1.15">Dolor sit amet, conse</div>
  <div class="abs" style="left:232px;top:73px;width:33px;height:68px;border:1.2px solid var(--ink);border-radius:4px;background:#fff;padding:11px 3px 0;font-size:4px;font-weight:500;line-height:1.15">Consec</div>
  <div class="foot"><span class="sq"></span><span class="nm">BRISK FOUNDRY</span><span class="ln"></span><span class="pg">14</span></div>
</section>

<!-- Team -->
<section class="slide c2 r6">
  <div class="h"><b>Heading</b> Goes Here</div><div class="rule"></div>
  <div class="abs" style="left:28px;top:52px;width:262px;display:grid;grid-template-columns:repeat(4,1fr);column-gap:24px;text-align:center">
    <div><div style="height:9px;background:var(--ink)"></div><div role="img" aria-label="Portrait photo of team member" style="width:24px;height:24px;border-radius:50%;margin:-7px auto 0;background:linear-gradient(#c9ced6,#8f97a3);border:1.5px solid #fff"></div><div class="member-name blue">TOVAN ELMQUIST</div><div class="tiny" style="font-size:2.6px;color:#aaa">Ipsum dolor sit amet, cons ectetuer adipiscing elit, sed diam nonummy nibh euismod tincidunt</div><div class="tiny" style="font-size:2.6px;color:#aaa;margin-top:2px">ut laoreet dolore magna aliquam erat volutpat.</div></div>
    <div><div style="height:9px;background:var(--blue)"></div><div role="img" aria-label="Portrait photo of team member" style="width:24px;height:24px;border-radius:50%;margin:-7px auto 0;background:linear-gradient(#c9ced6,#8f97a3);border:1.5px solid #fff"></div><div class="member-name">RESSA QUILLON</div><div class="tiny" style="font-size:2.6px;color:#aaa">Ipsum dolor sit amet, cons ectetuer adipiscing elit, sed diam nonummy nibh euismod tincidunt</div><div class="tiny" style="font-size:2.6px;color:#aaa;margin-top:2px">ut laoreet dolore magna aliquam erat volutpat.</div></div>
    <div><div style="height:9px;background:var(--ink)"></div><div role="img" aria-label="Portrait photo of team member" style="width:24px;height:24px;border-radius:50%;margin:-7px auto 0;background:linear-gradient(#c9ced6,#8f97a3);border:1.5px solid #fff"></div><div class="member-name blue">TOVAN ELMQUIST</div><div class="tiny" style="font-size:2.6px;color:#aaa">Ipsum dolor sit amet, cons ectetuer adipiscing elit, sed diam nonummy nibh euismod tincidunt</div><div class="tiny" style="font-size:2.6px;color:#aaa;margin-top:2px">ut laoreet dolore magna aliquam erat volutpat.</div></div>
    <div><div style="height:9px;background:var(--blue)"></div><div role="img" aria-label="Portrait photo of team member" style="width:24px;height:24px;border-radius:50%;margin:-7px auto 0;background:linear-gradient(#c9ced6,#8f97a3);border:1.5px solid #fff"></div><div class="member-name">RESSA QUILLON</div><div class="tiny" style="font-size:2.6px;color:#aaa">Ipsum dolor sit amet, cons ectetuer adipiscing elit, sed diam nonummy nibh euismod tincidunt</div><div class="tiny" style="font-size:2.6px;color:#aaa;margin-top:2px">ut laoreet dolore magna aliquam erat volutpat.</div></div>
  </div>
  <div class="foot"><span class="sq"></span><span class="nm">BRISK FOUNDRY</span><span class="ln"></span><span class="pg">15</span></div>
</section>

<!-- Thank you -->
<section class="slide c3 r6">
  <div class="abs" style="left:0;top:23px;width:307px;height:127px;background:var(--panel)"></div>
  <div class="abs" style="left:36px;top:78px;display:flex;align-items:center;gap:5px;color:#fff">
    <span style="width:21px;height:21px;background:var(--blue)"></span>
    <span style="font-size:12px;font-weight:700">BRISK FOUNDRY</span>
  </div>
  <div class="abs" style="left:169px;top:43px;color:#fff;font-size:19px;font-weight:800;line-height:1">Thank You</div>
  <div class="abs" style="left:169px;top:76px;color:#fff;font-size:4.5px;line-height:1.2">
    <div style="display:flex;gap:5px;align-items:center"><svg width="8" height="8" viewBox="0 0 8 8"><path d="M1.5 .5 L3 .5 L3.6 2.4 L2.6 3.2 Q3.4 4.8 4.9 5.5 L5.7 4.5 L7.5 5.1 L7.5 6.7 Q4 7.5 1.5 5 Q.2 3 .5 1.5 Z" fill="#1f3ff2"/></svg><span style="border-left:.6px solid #fff;padding-left:4px">+18 2000 4410 0000<br>+18 2000 4410 0000</span></div>
    <div style="display:flex;gap:5px;align-items:center;margin-top:8px"><svg width="8" height="8" viewBox="0 0 8 8"><path d="M.5 3.5 L7.5 .5 L4.5 7.5 L3.5 4.5 Z" fill="#1f3ff2"/></svg><span style="border-left:.6px solid #fff;padding-left:4px">www.brisk-foundry.net<br>hello@brisk-foundry.net</span></div>
    <div style="display:flex;gap:5px;align-items:center;margin-top:8px"><svg width="8" height="8" viewBox="0 0 8 8"><path d="M4 .5 L7.5 4 L6.5 4 L6.5 7.5 L1.5 7.5 L1.5 4 L.5 4 Z" fill="#1f3ff2"/></svg><span style="border-left:.6px solid #fff;padding-left:4px">1234 Street name, town/city,<br>state/country, post/zip 012345.</span></div>
  </div>
</section>

</main>
</body>
</html>
```